Business Card - high end, modern health care

Hey designers!

We need a double sided business card for the boutique, cutting edge physical therapy rehabilitation centre in Sydney's Northern Beaches.

With the most qualified physios in the area The Harbourline Motion Clinic does what other physiotherapy practices do not, we take our time with our patients giving them longer appointments, better physios and therefor faster results!

We guarantee that the service people receive at THMC will be unparalleled.

Hence we need a business card to reflect our modern, boutique, high end service. The final design needs to reflect that we are in a class of our own yet with the feel of beachside retreat.

Below I have attached our logo in both blue on white and white on blue. The exact colour is;
and the font that we have used in our logo is Tex Gyre Aventador.

I like the idea of the blue as the main colour as it is more eye catching and our signage onto the main road will be in this blue and in the interest of consistency across marketing the blue needs to be a part of the design. However I would appreciate a few designs onto a wooden background as this is a visual theme within the fitout of the practice.

The design needs to be of standard size (91x55mm).

Target Market(s)

We target people who have an end outcome in mind and those who have had poor experiences with other providers and ensure that everyone gets the care that they deserve with a premium service that is tailored to the individuals circumstances. As a premium service, the target market is highly educated, business and tech savvy with the additional target market of elderly people who have self funded their retirement and see value in paying for the best ongoing rehabilitation to maintain independence.

Industry/Entity Type

Physical Therapy

Contact Information for Business Card

Name, designation( Titled Musculoskeletal Physiotherapist... there will also be those in the company that have multiple designations ie 5 or 6 words long), phone number, email, facebook, instagram, address

Font styles to use
Sans Serif

Colors

Designer to choose colors to be used in the design.

Requirements
Must have
• Front - The logo as large as possible, blue or wooden theme, and all of the important details.
• Back - A blank space/lines on which to write appointment times (no "Appointment, date, time" etc.)
Nice to have
• facebook url
• logos for facebook and instagram
• Mini logos for the phone and email?

```html
<!DOCTYPE html>
<html lang="en">
<head>
<meta charset="utf-8">
<title>The Harbourline Motion Clinic – Business Card</title>
<link rel="stylesheet" href="https://fonts.googleapis.com/css2?family=Montserrat:wght@400;500;600;700&display=swap">
<style>
  :root {
    --brand-blue: #0450a3;
    --paper: #f3f3f2;
    --backdrop: #c9c9c9;
    --ink: #1e1e1e;
    --white: #ffffff;
  }
  * { margin: 0; padding: 0; box-sizing: border-box; }
  html, body {
    width: 1200px; height: 1001px; overflow: hidden;
    background: var(--backdrop);
    font-family: "Montserrat", sans-serif;
  }
  .canvas { position: relative; width: 1200px; height: 1001px; }
  .card {
    position: absolute; left: 339px; width: 525px; height: 299px;
    box-shadow: 6px 10px 18px rgba(0,0,0,0.25);
  }
  .card--front { top: 163px; background: var(--brand-blue); }
  .card--back { top: 538px; background: var(--paper); }

  .brand { position: absolute; display: flex; align-items: center; }
  .brand__dot { border-radius: 50%; flex: none; }
  .brand__name {
    font-weight: 700; text-transform: uppercase; line-height: 1.08;
    letter-spacing: 0.02em;
  }
  .card--front .brand { left: 108px; top: 122px; }
  .card--front .brand__dot { width: 54px; height: 54px; background: var(--white); margin-right: 12px; }
  .card--front .brand__name { color: var(--white); font-size: 24px; }

  .card--back .brand { left: 27px; top: 131px; }
  .card--back .brand__dot { width: 38px; height: 38px; background: var(--brand-blue); margin-right: 9px; }
  .card--back .brand__name { color: var(--brand-blue); font-size: 16.5px; }

  .divider {
    position: absolute; left: 263px; top: 85px; width: 1.5px; height: 130px;
    background: var(--brand-blue);
  }
  .contact { position: absolute; left: 280px; top: 96px; color: var(--ink); }
  .contact__name { font-size: 17px; letter-spacing: 0.08em; font-weight: 400; }
  .contact__name strong { font-weight: 700; }
  .contact__role {
    font-size: 10px; letter-spacing: 0.32em; color: var(--brand-blue);
    margin-top: 1px; font-weight: 500;
  }
  .contact__address { font-size: 9px; line-height: 1.25; margin-top: 12px; font-weight: 500; }
  .contact__list { list-style: none; margin-top: 12px; }
  .contact__item {
    display: flex; align-items: center; font-size: 11px; font-weight: 500;
    letter-spacing: 0.03em; height: 18.5px;
  }
  .contact__item svg { width: 11px; height: 11px; margin-right: 7px; flex: none; }
</style>
</head>
<body>
<main class="canvas">
  <section class="card card--front" aria-label="Card front">
    <div class="brand">
      <span class="brand__dot"></span>
      <p class="brand__name">The Harbourline<br>Motion Clinic</p>
    </div>
  </section>

  <section class="card card--back" aria-label="Card back">
    <div class="brand">
      <span class="brand__dot"></span>
      <p class="brand__name">The Harbourline<br>Motion Clinic</p>
    </div>
    <span class="divider"></span>
    <div class="contact">
      <p class="contact__name"><strong>CALLUM</strong> REYES</p>
      <p class="contact__role">DIRECTOR</p>
      <p class="contact__address">18 Pittwater Road, Suite 4<br>Manly, NSW 2095</p>
      <ul class="contact__list">
        <li class="contact__item">
          <svg viewBox="0 0 12 12" fill="none" stroke="#0450a3" stroke-width="1.1"><path d="M2.5 1.2l2 2-1.1 1.4a6 6 0 0 0 4 4l1.4-1.1 2 2-1.3 1.5C5.5 11 1 6.5 1 2.5z"/></svg>
          02 9876 5432
        </li>
        <li class="contact__item">
          <svg viewBox="0 0 12 12" fill="none" stroke="#0450a3" stroke-width="1.1"><rect x="0.8" y="2.3" width="10.4" height="7.4"/><path d="M0.8 2.3L6 6.6l5.2-4.3"/></svg>
          hello@harbourline.com
        </li>
        <li class="contact__item">
          <svg viewBox="0 0 12 12" fill="none" stroke="#0450a3" stroke-width="1"><circle cx="6" cy="6" r="5"/><ellipse cx="6" cy="6" rx="2.2" ry="5"/><path d="M1 6h10M2 3.3h8M2 8.7h8"/></svg>
          www.harbourline.com
        </li>
      </ul>
    </div>
  </section>
</main>
</body>
</html>
```